Norlo Tiered Food/Dessert Trays Spec Sheet

We need an elegant spec sheet template to use with our food/dessert trays. This will accompany the item when it ships out and on the web. It is something we would like to email our customers when they are considering our different banquet trays. It is important that it does not look too retail. We are the manufacturer and do not sell retail. We are business to business. It needs to help a salesman make a sale and look elegant enough while conveying the info to them.
Updates

Target Market(s)

Banquet Halls, Caterers, Country Clubs, Wedding and event centers.

Industry/Entity Type

Event

Font styles to use
Serif
Decorative
Script

Requirements
Must have
• All the copy in the word doc. Also use the model name as the heading at the top of the sheet
Nice to have
• An elegant but professional look
Should not have
• Not too busy

```html
<!DOCTYPE html>
<html lang="en">
<head>
<meta charset="utf-8">
<title>Norlo Grand Deluxe Spec Sheet</title>
<link href="https://fonts.googleapis.com/css2?family=Cinzel:wght@400;600&family=Open+Sans:wght@400;600;700&display=swap" rel="stylesheet">
<style>
:root{
  --backdrop:#d9dadb;
  --sheet:#ffffff;
  --sheet-fade:#e9e9ea;
  --ink:#3a3a3a;
  --ink-soft:#5a5a5a;
  --rule:#9a9a9a;
  --photo-warm:#7a5544;
  --photo-dark:#3b2a22;
  --photo-glow:#c69a73;
  --logo:#ffffff;
}
*{box-sizing:border-box;margin:0;padding:0}
html,body{width:1200px;height:900px;overflow:hidden}
body{background:var(--backdrop);font-family:"Open Sans",Arial,sans-serif;color:var(--ink);position:relative}
.sheet{position:absolute;left:320px;top:30px;width:560px;height:840px;background:linear-gradient(180deg,var(--sheet) 55%,var(--sheet-fade) 100%);box-shadow:0 6px 22px rgba(0,0,0,.25);overflow:hidden}
.hero{position:absolute;left:0;top:0;width:560px;height:500px}
.brand{position:absolute;left:150px;top:62px;display:flex;align-items:center;gap:10px;color:var(--logo);font-family:"Cinzel",serif;font-weight:400;font-size:22px;letter-spacing:2px;line-height:1}
.brand-mark{width:26px;height:26px;background:var(--logo)}
.intro{position:absolute;left:40px;top:512px;width:480px;font-size:10.2px;line-height:1.75;color:var(--ink)}
.intro strong{font-weight:700}
.details{position:absolute;left:40px;top:590px;width:480px;display:flex;gap:30px}
.col{flex:1;font-size:9px;line-height:1.95;color:var(--ink-soft)}
.col h3{font-size:9.2px;font-weight:700;color:var(--ink);margin-bottom:2px}
.col ul{list-style:none}
.specs{padding-left:16px}
.footer-rule{position:absolute;left:40px;top:766px;width:480px;border-top:1px solid var(--rule)}
.company{position:absolute;left:60px;top:782px;font-size:13px;color:var(--ink)}
.contact{position:absolute;left:300px;top:774px;font-size:7px;line-height:2.1;color:var(--ink-soft);display:grid;grid-template-columns:auto auto;column-gap:16px}
</style>
</head>
<body>
<article class="sheet">
  <svg class="hero" viewBox="0 0 560 500" width="560" height="500">
    <defs>
      <linearGradient id="banquetTone" x1="0" y1="0" x2="1" y2="1">
        <stop offset="0" stop-color="var(--photo-dark)"/>
        <stop offset=".5" stop-color="var(--photo-warm)"/>
        <stop offset="1" stop-color="var(--photo-glow)"/>
      </linearGradient>
      <linearGradient id="standTone" x1="0" y1="0" x2="0" y2="1">
        <stop offset="0" stop-color="#f4f4f4"/>
        <stop offset=".5" stop-color="#c9c7c2"/>
        <stop offset="1" stop-color="#ebeae7"/>
      </linearGradient>
    </defs>
    <rect width="560" height="500" fill="url(#banquetTone)" role="img" aria-label="Photo of a banquet table set with pink and white roses, glassware and candlelight"/>
    <polygon points="0,330 280,500 0,500" fill="#f1f1f2" opacity=".85"/>
    <polygon points="560,300 280,500 560,500" fill="#ffffff" opacity=".9"/>
    <polygon points="0,400 280,500 560,380 560,500 0,500" fill="#ffffff"/>
    <polygon points="280,140 420,220 420,380 280,460 140,380 140,220" fill="#ffffff"/>
    <rect x="180" y="190" width="200" height="230" fill="url(#standTone)" role="img" aria-label="Product photo of the three-tier polished steel buffet stand"/>
  </svg>
  <div class="brand"><span class="brand-mark"></span>NORLO FOUNTAINS</div>

  <p class="intro"><strong>The Grand Deluxe Three-</strong>Tier Buffet Stand Features Polished, Stainless Steel, Trays and Base. It Also Features Bright Nickel Plated Silver Columns. This Eye Catching Stand with its Large Tray Sizes Make it an Excellent Choice for Serving Large Groups at Banquets, Buffets or any Catering Operation. Create Stunning Appetizers, Finger Foods, Main Courses and More. This Stand is a True Caterers Dream...</p>

  <section class="details">
    <div class="col specs">
      <h3>Product Specs:</h3>
      <ul>
        <li>Model # : GD24-1814-S</li>
        <li>Model Name: Grand Deluxe</li>
        <li>Height: 33"</li>
        <li>Tray Sizes: 24", 18", 14"</li>
        <li>Product Weight: 20lbs</li>
        <li>Shipping Weight: 28lbs</li>
        <li>Shipping Dimensions: 27 x 27 x 10 inches</li>
      </ul>
    </div>
    <div class="col features">
      <h3>Features:</h3>
      <ul>
        <li>Designed for Repeated Commercial Use</li>
        <li>High Polished Stainless Steel Trays &amp; Base</li>
        <li>Decorative Silver Bow Tie Trim on the Base</li>
        <li>Nickel Plated Silver Columns ( No Tarnish, No Polish )</li>
        <li>Self-Serving Buffet Station</li>
        <li>No Tools Needed for Assembly or Disassembly</li>
        <li>Breaks Down for Easy Clean Up and Storage</li>
        <li>1 Year Limited Warranty</li>
      </ul>
    </div>
  </section>

  <div class="footer-rule"></div>
  <p class="company">Norlo Fountain Sales, Inc.</p>
  <div class="contact">
    <span>Web: www.norlofountains.com</span><span>Phone: 800-555-0142</span>
    <span>Fax: 215-555-0187</span><span>Email: info@norlofountains.com</span>
  </div>
</article>
</body>
</html>
```